Holistic massage therapist

I need a business card for a business made by me, I m an holistic massage therapist, I 'm qualified in reflexology , indian head massage and sweedish body massage, I m working from home or mobile as well, i use massage as a therapy not as a beauty treatment, i m base in London.
I also offer skincare product such as creams or oils and blending with essential oil that I make my self they are completely natural and 100% use of organic product, all the product they are homemade by me.

Industry/Entity Type

Massage

Requirements
Must have
• image that express peace and quite as the massage is an anti stresful remedies for the everyday life

```html
<!DOCTYPE html>
<html lang="en">
<head>
<meta charset="utf-8">
<title>Holistic Massage Therapist – Business Card</title>
<link rel="stylesheet" href="https://fonts.googleapis.com/css2?family=Lato:wght@400;700&display=swap">
<style>
  :root {
    --backdrop: #c9c1b4;
    --card-white: #ffffff;
    --leaf-green: #9fc73c;
    --deep-green: #3f8a2c;
    --logo-tone-a: #e9f2d6;
    --logo-tone-b: #c7e08a;
    --ink-white: #ffffff;
  }
  html, body {
    margin: 0;
    width: 1200px;
    height: 1000px;
    overflow: hidden;
    background: var(--backdrop);
    font-family: "Lato", sans-serif;
  }
  .business-card {
    position: absolute;
    left: 230px;
    top: 275px;
    width: 740px;
    height: 450px;
    border-radius: 22px;
    overflow: hidden;
    background: var(--card-white);
    box-shadow: 0 18px 40px rgba(0,0,0,0.25);
  }
  .brand-area {
    position: absolute;
    left: 0; top: 0;
    width: 100%;
    height: 250px;
    background: var(--card-white);
  }
  .brand-mark {
    position: absolute;
    left: 270px;
    top: 34px;
    width: 200px;
    height: 150px;
    border-radius: 10px;
    background: radial-gradient(circle at 50% 45%, var(--logo-tone-b), var(--logo-tone-a) 75%);
  }
  .brand-title {
    position: absolute;
    left: 0; right: 0;
    top: 196px;
    margin: 0;
    text-align: center;
    font-size: 30px;
    font-weight: 700;
    color: var(--leaf-green);
  }
  .info-band {
    position: absolute;
    left: 0;
    top: 250px;
    width: 100%;
    height: 200px;
    background: var(--leaf-green);
    border-top: 7px solid var(--deep-green);
    color: var(--ink-white);
    text-align: center;
  }
  .therapist-name {
    margin: 10px 0 4px;
    font-size: 28px;
    font-weight: 700;
  }
  .services {
    margin: 0 0 10px;
    font-size: 18px;
    letter-spacing: 0.5px;
  }
  .contact-row {
    display: flex;
    justify-content: center;
    gap: 34px;
    font-size: 15px;
    font-weight: 700;
    margin-bottom: 14px;
  }
  .contact-item {
    display: flex;
    align-items: center;
    gap: 7px;
  }
  .contact-item svg { width: 15px; height: 15px; }
  .products-note {
    margin: 0 0 6px;
    font-size: 13px;
    letter-spacing: 0.3px;
  }
  .products-list {
    margin: 0;
    font-size: 18px;
    font-weight: 700;
  }
</style>
</head>
<body>
  <article class="business-card">
    <header class="brand-area">
      <div class="brand-mark" role="img" aria-label="Line drawing of a calm seated figure between two green leaf sprigs"></div>
      <h1 class="brand-title">Holistic Massage Therapist</h1>
    </header>
    <section class="info-band">
      <h2 class="therapist-name">Mara Ellis</h2>
      <p class="services">REFLEXOLOGY &bull; INDIAN HEAD MASSAGE &bull; SWEEDISH BODY MASSAGE</p>
      <div class="contact-row">
        <span class="contact-item">
          <svg viewBox="0 0 16 16" aria-hidden="true"><path fill="#fff" d="M3 1h3l1.5 4-2 1.3a9 9 0 0 0 4.2 4.2L11 8.5l4 1.5v3a2 2 0 0 1-2 2A13 13 0 0 1 1 3a2 2 0 0 1 2-2z"/></svg>
          555 555 0148
        </span>
        <span class="contact-item">
          <svg viewBox="0 0 16 16" aria-hidden="true"><rect x="1" y="3" width="14" height="10" fill="#fff"/><path d="M1 3l7 5 7-5" fill="none" stroke="#9fc73c" stroke-width="1.4"/></svg>
          mara@calmhands.net
        </span>
        <span class="contact-item">
          <svg viewBox="0 0 16 16" aria-hidden="true"><g fill="none" stroke="#fff" stroke-width="1.4"><circle cx="8" cy="8" r="6.5"/><ellipse cx="8" cy="8" rx="2.8" ry="6.5"/><path d="M1.5 8h13"/></g></svg>
          www.calmhands.net
        </span>
      </div>
      <p class="products-note">WE OFFER SKINCARE PRODUCTS 100% ORGANIC | HOMEMADE PRODUCTS</p>
      <p class="products-list">CREAMS | OILS ETC.</p>
    </section>
  </article>
</body>
</html>
```